Business Card and Stationery for Interior Design Company
Silver Kettle Design
Designers,
On the back of my card on want the following services listed:
Interior Decorating
Room Redesign
Space Planning
Paint Color Selection
Furnishings & Accessories
The fonts used in the logo are as follows:
fonts:
Kozuka Mincho Pr6N M
Miss Le Gatees (modified)
RT/KPF/JN Team
My tagline "Design with Vision" does NOT have to be the same font as the original logo font. Neither does my Name. In fact, tagline should probably be italic and my Name I'd like to see perhaps in a similar script font like the word INTERIOR.

```html
<!DOCTYPE html>
<html lang="en">
<head>
<meta charset="utf-8">
<title>Silver Kettle Design — Business Card</title>
<link rel="stylesheet" href="https://fonts.googleapis.com/css2?family=Cormorant+Garamond:wght@500&family=Great+Vibes&family=Libre+Baskerville:ital@0;1&display=swap">
<style>
  :root {
    --page: #eeeeee;
    --card: #ffffff;
    --stripe: #f1f1f1;
    --teal: #7ccfc9;
    --teal-deep: #5bb9b3;
    --ink: #3a2f2a;
    --brown: #5a4638;
    --gold: #d8b46a;
    --muted: #b7c9c7;
  }
  * { box-sizing: border-box; margin: 0; padding: 0; }
  html, body { width: 1200px; height: 1025px; overflow: hidden; background: var(--page); }
  .stage { position: relative; width: 1200px; height: 1025px; }

  .card {
    position: absolute;
    top: 125px;
    width: 490px;
    height: 836px;
    background: repeating-linear-gradient(90deg, var(--card) 0 34px, var(--stripe) 34px 68px);
    box-shadow: 0 6px 18px rgba(0,0,0,.14);
  }
  .card--front { left: 80px; }
  .card--back { left: 630px; }

  .card__frame {
    position: absolute; inset: 18px;
    border: 2px solid var(--teal);
  }

  .logo { position: absolute; left: 0; right: 0; text-align: center; }
  .logo__art {
    display: block; margin: 0 auto;
    background: linear-gradient(135deg, #f6efe0 0%, #e9d9b4 40%, #9fd8d3 75%, #6fc3bd 100%);
    border-radius: 4px;
  }
  .logo__name {
    font-family: "Cormorant Garamond", serif;
    font-weight: 500;
    color: var(--brown);
    line-height: 1.05;
  }

  .card--front .logo { top: 110px; }
  .card--front .logo__art { width: 200px; height: 150px; }
  .card--front .logo__name { font-size: 50px; margin-top: 16px; }

  .person {
    position: absolute; top: 555px; left: 0; right: 0; text-align: center;
    font-family: "Great Vibes", cursive; font-size: 40px; color: var(--teal-deep);
  }
  .contact {
    position: absolute; top: 640px; left: 0; right: 0; text-align: center;
    font-family: "Libre Baskerville", serif; color: var(--ink);
  }
  .contact__phone { font-size: 21px; letter-spacing: 1px; margin-bottom: 12px; }
  .contact__line { font-size: 15px; letter-spacing: .5px; line-height: 1.6; }

  .ribbon {
    position: absolute; left: 42px; right: 42px; bottom: 48px; height: 42px;
    background: var(--teal);
    border-left: 6px solid var(--gold);
    border-right: 6px solid var(--gold);
    display: flex; align-items: center; justify-content: center;
    font-family: "Libre Baskerville", serif; font-style: italic;
    color: #fff; font-size: 18px; letter-spacing: 2px;
  }

  .card--back .logo { top: 70px; }
  .card--back .logo__art { width: 150px; height: 112px; }
  .card--back .logo__name { font-size: 36px; margin-top: 12px; }

  .services {
    position: absolute; top: 395px; left: 22px; right: 22px; height: 320px;
    border-top: 2px solid var(--teal);
    border-bottom: 2px solid var(--teal);
    border-left: 2px solid var(--teal);
    text-align: center;
  }
  .services__title {
    margin-top: -14px; display: inline-block; padding: 0 10px;
    font-family: "Libre Baskerville", serif; font-style: italic;
    font-size: 21px; letter-spacing: 2.5px; color: var(--teal-deep);
    background: var(--card);
  }
  .services__list {
    list-style: none; margin-top: 48px;
    font-family: "Libre Baskerville", serif; font-size: 19px;
    color: var(--ink); line-height: 1.72;
  }
  .web {
    position: absolute; bottom: 78px; left: 0; right: 0; text-align: center;
    font-family: "Libre Baskerville", serif; font-size: 13px;
    letter-spacing: 2px; color: var(--muted);
  }
</style>
</head>
<body>
<main class="stage">
  <section class="card card--front">
    <div class="card__frame"></div>
    <div class="logo">
      <div class="logo__art" role="img" aria-label="Illustration of a dresser, chandelier and teal sofa with gold accents"></div>
      <p class="logo__name">Silver Kettle<br>Design</p>
    </div>
    <p class="person">Maren Holloway</p>
    <div class="contact">
      <p class="contact__phone">555.014.2287</p>
      <p class="contact__line">maren@silverkettledesign.com</p>
      <p class="contact__line">www.silverkettledesign.com</p>
    </div>
    <div class="ribbon">Design with Vision</div>
  </section>

  <section class="card card--back">
    <div class="logo">
      <div class="logo__art" role="img" aria-label="Illustration of a dresser, chandelier and teal sofa with gold accents"></div>
      <p class="logo__name">Silver Kettle<br>Design</p>
    </div>
    <div class="services">
      <h2 class="services__title">Design with Vision</h2>
      <ul class="services__list">
        <li>Interior Decorating</li>
        <li>Room Redesign</li>
        <li>Space Planning</li>
        <li>Paint &amp; Fabric Selection</li>
        <li>Furnishings &amp; Accessories</li>
      </ul>
    </div>
    <p class="web">www.silverkettledesign.com</p>
  </section>
</main>
</body>
</html>
```